Pemberly & Associates Tax Services

Need an eye catching advertisement/lead generating design for prospects interesting in professional tax planning and tax preparation services. Ideas for
Sample Advertising Language is below:

We are accepting new clients!!
We are affordable and have over 20 years of experience serving the tax needs of our clientele.

Here are a few reasons you may want to contact us:

1. You want to learn how to maximize business deductions
2. You’re a high-income earner and want to learn ways to pay less in taxes
3. You have an interest in starting a business
4. You want to maximize rental property deductions
5. You have questions about maintaining a home office
6. You want to be updated periodically on tax law changes and tax planning strategies
7. You want to be represented by a tax expert before the IRS if you are subject to an audit

References available upon request.

Target Market(s)

Individuals, small businesses and startup business

Industry/Entity Type

Tax and Accounting Industry

Requirements
Nice to have
• Would like to develop a marketing campaign that can be used periodically to digitally generate leads, build email contact list of prospective clients who want to receive tax updates.

```html
<!DOCTYPE html>
<html lang="en">
<head>
<meta charset="utf-8">
<title>Pemberly &amp; Associates Tax Services – Accepting New Clients</title>
<link href="https://fonts.googleapis.com/css2?family=Bebas+Neue&family=Carlito:wght@400;700&display=swap" rel="stylesheet">
<style>
  :root {
    --brand-blue: #1e5b9a;
    --row-blue: #17467f;
    --brand-green: #1f9640;
    --panel-grey: #e1e3e5;
    --white: #ffffff;
  }
  * { margin: 0; padding: 0; box-sizing: border-box; }
  html, body { width: 789px; height: 1200px; overflow: hidden; background: var(--white); }
  .poster { position: relative; width: 789px; height: 1200px; background: var(--white); font-family: "Carlito", "Calibri", sans-serif; color: var(--brand-blue); }

  .hero { position: absolute; left: 17px; top: 17px; width: 753px; height: 556px; background: var(--panel-grey); overflow: hidden; }
  .hero-swoosh { position: absolute; left: 0; top: 0; width: 753px; height: 556px; }
  .hero-photo { position: absolute; left: 410px; top: 40px; width: 270px; height: 516px; border-radius: 120px 120px 0 0; background: linear-gradient(180deg, #d7dde3 0%, #b6cce0 40%, #9ab7d3 75%, #6f8fb2 100%); }

  .headline { position: absolute; left: 67px; top: 50px; font-family: "Bebas Neue", "Oswald", sans-serif; font-weight: 400; color: var(--brand-blue); font-size: 84px; line-height: 87px; letter-spacing: 0; }
  .headline .cta { display: block; color: var(--brand-green); font-size: 124px; line-height: 118px; margin-top: 6px; }

  .intro { position: absolute; left: 0; top: 588px; width: 789px; text-align: center; }
  .intro-line { font-size: 23px; font-weight: 700; line-height: 28px; }
  .intro-strong { font-size: 44px; font-weight: 700; line-height: 48px; }

  .reasons { position: absolute; left: 75px; top: 681px; width: 642px; height: 276px; background: var(--brand-blue); border-radius: 28px; color: var(--white); }
  .reasons-title { text-align: center; font-size: 20px; font-weight: 700; margin-top: 9px; line-height: 26px; padding-left: 8px; }
  .reasons-list { list-style: none; margin: 7px 0 0 43px; width: 553px; }
  .reasons-list li { position: relative; font-size: 17.5px; line-height: 24.6px; padding: 0 10px 0 44px; }
  .reasons-list li::before { content: ""; position: absolute; left: 26px; top: 10px; width: 6px; height: 6px; border-radius: 50%; background: var(--white); }
  .reasons-list li.striped { background: var(--row-blue); padding-top: 0; }

  .call-to-action { position: absolute; left: 0; top: 964px; width: 789px; text-align: center; font-size: 42px; font-weight: 700; line-height: 50px; }

  .brand { position: absolute; left: 105px; top: 1066px; display: flex; align-items: center; gap: 12px; }
  .brand-dot { width: 34px; height: 34px; border-radius: 50%; background: var(--brand-blue); flex: none; }
  .brand-name { font-size: 22px; font-weight: 700; line-height: 25px; color: var(--brand-blue); }

  .contact { position: absolute; left: 440px; top: 1050px; font-size: 17px; font-weight: 700; line-height: 20.6px; font-style: normal; }
</style>
</head>
<body>
<main class="poster">
  <section class="hero">
    <svg class="hero-swoosh" viewBox="0 0 753 556" aria-hidden="true">
      <path fill="#ffffff" fill-rule="evenodd" d="M380 10 A330 330 0 1 0 381 10 Z M440 40 A280 285 0 1 1 439 40 Z"/>
      <rect x="0" y="0" width="753" height="6" fill="#e1e3e5"/>
    </svg>
    <div class="hero-photo" role="img" aria-label="Smiling man in a light denim shirt giving a thumbs up"></div>
    <h1 class="headline">Professional<br>tax planners<br>need not be<br>expensive!<span class="cta">Try us!</span></h1>
  </section>

  <header class="intro">
    <p class="intro-line">We have over 20 years of experience. We are affordable.</p>
    <p class="intro-strong">We are accepting new clients.</p>
  </header>

  <section class="reasons">
    <h2 class="reasons-title">Here are a few reasons why you may want to contact us:</h2>
    <ul class="reasons-list">
      <li class="striped">Learn&nbsp; how to maximize business deductions</li>
      <li>Learn ways on how to pay less taxes if you’re<br>a high-income earner</li>
      <li class="striped">You want to start a business</li>
      <li>You want to maximize rental property deductions</li>
      <li class="striped">You have questions about maintaining a home office</li>
      <li>You want to be updated regularly on tax laws changes and tax<br>planning strategies</li>
      <li class="striped">You want a tax expert to represent you before the IRS</li>
    </ul>
  </section>

  <p class="call-to-action">Give us a call or send us an email.</p>

  <div class="brand">
    <span class="brand-dot" aria-hidden="true"></span>
    <span class="brand-name">Pemberly &amp; Associates LLC<br>Tax &amp; Business Services</span>
  </div>

  <address class="contact">
    4187 Alder Creek Rd., Suite 210-118<br>
    Fairbrook, CA 95812<br>
    (555) 014-2290<br>
    www.ledgerpoint@mailbox.com
  </address>
</main>
</body>
</html>
```